Quillfern Nightclub Flyer (Updated)

Flyer for facebook, square is fine, or rectangular. Here is the text:
QUILLFERN
Nightclub + Lounge
presents

SPLIT DECK WEDNESDAY
Nov 29 2018

CLUB FLOOR:
GORDY B2B RALPH
THEODORE BRUSKVIK

LOUNGE:
OTIS B2B HALF TIDE
COPPER FENWICK

Powered by HALVERN Acoustics
4716 Larchmere Avenue 21+ 9pm-2am
quillfernvenue-example.com for VIP booth inquiries

Target Market(s)

Nightclub

Industry/Entity Type

Night Club

Font styles to use
Sans Serif

Colors

Designer to choose colors to be used in the design.

Requirements
Must have
• All the text listed, and plz keep the theme of the attached files. We want to stay consistent with the Quillfern brand
Nice to have
• Try to stay with the theme from the attachments
Should not have
• Dont' stray to far from the general theme we have from the attachments

```html
<!DOCTYPE html>
<html lang="en">
<head>
<meta charset="utf-8">
<title>Quillfern Nightclub + Lounge – Split Deck Wednesday</title>
<link rel="stylesheet" href="https://fonts.googleapis.com/css2?family=Playfair+Display:wght@400;700&family=Open+Sans:wght@400;600&family=Open+Sans+Condensed:wght@300&display=swap">
<style>
  :root {
    --page: #ffffff;
    --ink: #050505;
    --white: #ffffff;
    --gold: #d9a066;
    --gold-deep: #8a5a2b;
    --gold-light: #f0c98f;
    --label-grey: #7a7a7a;
    --rule: #8c8c8c;
  }
  * { margin: 0; padding: 0; box-sizing: border-box; }
  html, body { width: 1200px; height: 608px; overflow: hidden; background: var(--page); }
  .canvas { position: relative; width: 1200px; height: 608px; background: var(--page); }
  .banner {
    position: absolute; left: 0; top: 62px; width: 1200px; height: 483px;
    background: var(--ink); overflow: hidden;
    font-family: "Open Sans", Arial, sans-serif; color: var(--white);
  }
  .ornament-area {
    position: absolute; left: 0; top: 0; width: 343px; height: 483px;
    background: radial-gradient(ellipse 100% 60% at 0% 50%, var(--gold-light) 0%, var(--gold) 30%, var(--gold-deep) 62%, var(--ink) 100%);
    opacity: 0.9;
  }
  .logo-tile {
    position: absolute; left: 362px; top: 16px; width: 153px; height: 150px;
    background: #f7f8fa;
    display: flex; flex-direction: column; align-items: center; justify-content: center; gap: 12px;
  }
  .logo-tile .dot { width: 30px; height: 30px; border-radius: 50%; background: #c9c25f; }
  .logo-tile .name {
    font-family: "Playfair Display", Georgia, serif; font-weight: 400;
    font-size: 18px; color: #4a4040; letter-spacing: 0.5px;
  }
  .venue-title {
    position: absolute; left: 552px; top: 22px;
    font-family: "Playfair Display", Georgia, serif; font-weight: 400;
    font-size: 78px; line-height: 1; letter-spacing: 1px;
  }
  .venue-subtitle {
    position: absolute; left: 556px; top: 122px;
    font-size: 25px; letter-spacing: 4px; line-height: 1;
  }
  .presents {
    position: absolute; left: 362px; width: 838px; top: 190px; text-align: center;
    font-size: 24px; color: var(--gold); line-height: 1;
  }
  .rule { position: absolute; height: 1px; background: var(--rule); }
  .rule-top { left: 362px; right: 0; top: 227px; }
  .rule-bottom { left: 362px; right: 0; top: 411px; }
  .rule-event { left: 514px; width: 650px; top: 301px; background: #2b2b2b; }
  .rule-event-end { position: absolute; left: 1166px; top: 298px; width: 7px; height: 7px; border-radius: 50%; border: 1px solid var(--gold); }
  .event-date {
    position: absolute; left: 363px; top: 250px; width: 135px; height: 52px;
    display: flex; align-items: center; justify-content: center;
    font-family: "Playfair Display", Georgia, serif; font-weight: 700; font-size: 33px;
    background: linear-gradient(180deg, var(--gold-light), var(--gold-deep));
    -webkit-background-clip: text; background-clip: text; color: transparent;
  }
  .event-name { position: absolute; left: 514px; top: 259px; font-size: 34px; line-height: 1; }
  .lineup-label {
    position: absolute; top: 345px; font-size: 15px; letter-spacing: 3.5px;
    color: var(--label-grey); line-height: 1;
  }
  .lineup-label.club { left: 362px; }
  .lineup-label.lounge { left: 782px; }
  .lineup-acts {
    position: absolute; top: 340px; list-style: none;
    font-family: "Open Sans Condensed", "Arial Narrow", sans-serif; font-weight: 300;
    font-size: 21px; line-height: 31px; letter-spacing: -0.3px;
  }
  .lineup-acts.club { left: 509px; }
  .lineup-acts.lounge { left: 894px; }
  .venue-info {
    position: absolute; left: 362px; top: 428px;
    font-size: 17.5px; line-height: 24px; color: var(--gold);
  }
</style>
</head>
<body>
<main class="canvas">
  <section class="banner">
    <div class="ornament-area" role="img" aria-label="Gold mandala ornament on black"></div>

    <div class="logo-tile">
      <span class="dot"></span>
      <span class="name">QUILLFERN</span>
    </div>

    <h1 class="venue-title">QUILLFERN</h1>
    <p class="venue-subtitle">NIGHTCLUB + LOUNGE</p>

    <p class="presents">PRESENTS :</p>
    <div class="rule rule-top"></div>

    <div class="event-date">NOV 29</div>
    <h2 class="event-name">Split Deck Wednesday</h2>
    <div class="rule rule-event"></div>
    <span class="rule-event-end"></span>

    <span class="lineup-label club">CLUBFLOOR:</span>
    <ul class="lineup-acts club">
      <li>GORDY B2B RALPH</li>
      <li>THEODORE BRUSKVIK</li>
    </ul>

    <span class="lineup-label lounge">LOUNGE:</span>
    <ul class="lineup-acts lounge">
      <li>OTIS B2B HALF TIDE</li>
      <li>COPPER FENWICK</li>
    </ul>

    <div class="rule rule-bottom"></div>

    <p class="venue-info">Powered by HALVERN Acoustics , 4716 Larchmere Avenue 21+ 9pm-2am , quillfernvenue-example.com<br>for VIP booth inquiries</p>
  </section>
</main>
</body>
</html>
```